WEDDING BROCHURE FOR BOUTIQUE VINEYARD

We need a wedding brochure to be designed for a boutique vineyard in NSW, Australia.  The successful design will go on to win a number of designs keeping in the same theme - DL Flyer design, price list and some signage.
We have selected a number of photos that you can use.  We would like this to be 4 pages in total so that we can print A3 and then have this folded in half.
I would suggest you look at our website www.pallowmere.com.au for a feel of the property and currrent branding.  We like a clean feel with white and dark grey fonts.
Attached is a copy of text, logo, photos etc.  Photos can be edited as you feel necessary.  Wedding photos have been bought from Pixvana and there is a preference to use these.
Also attached is the current DL flyer that will be replaced as part of second piece or work.  It shows an example of map as required on back page.

Updates
Please see the two examples of what i want.  Clean design.  White background with dark grey fonts.  Photos should be kept as is and boxed together.  Premium and upmarket is what we are trying to achieve.
http://www.tavelbrook.com.au/client-assets/pdf/march2014%20TB%20WeddingCompendium_Update_1.pdf

Target Market(s)
Potential wedding customers
Industry/Entity Type
Boutique
Colors
Designer to choose colors to be used in the design.
Requirements
Must have
- Flyer must have an illustrated map indicating where the property is.  This maybe on the last page along with contact details.  You can see the link to our property through the following google maps link https://www.mapvista.com.au/maps/place/Pallowmere+Estate/@-33.000000,150.000000,17z/data=!3m1!4b1!4m2!3m1!1s0x0000000000000000:0x0000000000000000
This map must include neighbouring towns of Blackheath, Katoomba and Leura.

```html
<!DOCTYPE html>
<html lang="en">
<head>
<meta charset="UTF-8">
<title>Pallowmere Estate – Weddings</title>
<link href="https://fonts.googleapis.com/css2?family=Open+Sans:wght@400;600&display=swap" rel="stylesheet">
<style>
  :root {
    --navy: #3e5ea9;
    --sky: #3bb9ea;
    --sky-mid: #4a95d6;
    --text-grey: #6b6b6b;
    --white: #ffffff;
    --photo-house: #7f9a6c;
    --photo-glass: #d9dcd6;
    --photo-flowers: #8e8a84;
  }
  * { margin: 0; padding: 0; box-sizing: border-box; }
  html, body { width: 848px; height: 1200px; overflow: hidden; background: var(--white); }
  body { font-family: "Open Sans", Arial, sans-serif; }
  .page { position: relative; width: 848px; height: 1200px; overflow: hidden; background: var(--white); }

  .top-band { position: absolute; left: 0; top: 0; width: 848px; height: 237px; background: var(--navy); }
  .top-band .accent-bar { position: absolute; left: 0; top: 69px; width: 287px; height: 18px; background: var(--sky); }
  .section-title { font-weight: 400; font-size: 28px; line-height: 1; }
  .marquees-title { position: absolute; left: 303px; top: 64px; color: var(--white); }
  .marquees-copy { position: absolute; left: 40px; top: 110px; width: 396px; color: var(--white); font-size: 13.4px; line-height: 18.8px; text-align: justify; }
  .house-photo { position: absolute; left: 468px; top: 69px; width: 380px; height: 123px; background: linear-gradient(180deg, #9fb6cf 0%, #c9cdc4 40%, var(--photo-house) 75%, #5d7a4f 100%); border-left: 6px solid var(--sky); }

  .glass-photo { position: absolute; left: 40px; top: 238px; width: 304px; height: 301px; background: linear-gradient(90deg, #c7ccc4 0%, var(--photo-glass) 45%, #e6dfb8 65%, #cfd3cf 100%); }
  .beverages-head { position: absolute; left: 40px; top: 539px; width: 304px; height: 47px; background: var(--navy); }
  .beverages-head .section-title { position: absolute; left: 14px; top: 10px; color: var(--white); }
  .beverages-box { position: absolute; left: 40px; top: 586px; width: 304px; height: 135px; background: var(--sky); padding: 9px 14px 0 14px; color: var(--white); font-size: 13.4px; line-height: 18.8px; text-align: justify; }

  .flowers-photo { position: absolute; left: 40px; top: 791px; width: 304px; height: 236px; background: radial-gradient(ellipse at 55% 55%, #f3f1ea 0%, #d8d6cf 35%, var(--photo-flowers) 75%, #6d6963 100%); }
  .flowers-base { position: absolute; left: 40px; top: 1027px; width: 304px; height: 7px; background: var(--navy); }

  .terms-title { position: absolute; left: 392px; top: 283px; color: var(--navy); }
  .terms-bar { position: absolute; left: 667px; top: 289px; width: 181px; height: 18px; background: var(--sky); }
  .terms-list { position: absolute; left: 392px; top: 338px; width: 424px; list-style: none; display: flex; flex-direction: column; gap: 18px; }
  .terms-list li { display: flex; align-items: flex-start; gap: 8px; color: var(--text-grey); font-size: 14px; line-height: 18.8px; text-align: justify; }
  .terms-list li.tick-low { align-items: flex-end; }
  .terms-list svg { flex: 0 0 16px; width: 16px; height: 16px; margin-top: 1.5px; margin-bottom: 1.5px; }
  .terms-list span { flex: 1; }

  .swoosh { position: absolute; left: 0; top: 0; }
  .site-url { position: absolute; left: 600px; top: 1143px; color: var(--white); font-size: 16px; letter-spacing: 0.3px; }
</style>
</head>
<body>
<div class="page">
  <header class="top-band">
    <div class="accent-bar"></div>
    <h2 class="section-title marquees-title">Marquees</h2>
    <p class="marquees-copy">There are a number of locations on the Estate where marquees can be positioned. The largest possible location will house a 10 x 20m marquee giving enough room to comfortably seat up to 200 guests.</p>
    <div class="house-photo" role="img" aria-label="Photo of the estate homestead with a veranda and garden path"></div>
  </header>

  <div class="glass-photo" role="img" aria-label="Photo of a row of champagne flutes filled with sparkling wine"></div>
  <div class="beverages-head"><h2 class="section-title">Beverages</h2></div>
  <p class="beverages-box">There are a number of locations on the Estate where marquees can be positioned. The largest possible location will house a 10 x 20m marquee giving enough room to comfortably seat up to 200 guests.</p>

  <div class="flowers-photo" role="img" aria-label="Photo of a white rose bridal bouquet on weathered timber"></div>
  <div class="flowers-base"></div>

  <h2 class="section-title terms-title">Terms &amp; Conditions</h2>
  <div class="terms-bar"></div>

  <svg width="0" height="0" style="position:absolute">
    <defs>
      <g id="tick">
        <circle cx="8" cy="8" r="8" fill="#3bb9ea"/>
        <path d="M4.4 8.3 L7 10.8 L11.8 5.6" fill="none" stroke="#fff" stroke-width="1.9" stroke-linecap="round" stroke-linejoin="round"/>
      </g>
    </defs>
  </svg>

  <ul class="terms-list">
    <li><svg viewBox="0 0 16 16"><use href="#tick"/></svg><span>$2,000 security bond payable 30 days before the wedding and refundable immediately after inspection</span></li>
    <li><svg viewBox="0 0 16 16"><use href="#tick"/></svg><span>$1,000 deposit to be paid upon securing your wedding date and the remainder payable 30 days prior to the wedding date</span></li>
    <li><svg viewBox="0 0 16 16"><use href="#tick"/></svg><span>All marquees, party hire or other non Pallowmere Estate property must be removed no later than a day after check out</span></li>
    <li><svg viewBox="0 0 16 16"><use href="#tick"/></svg><span>No more guests are to stay at either residence than there are beds provided</span></li>
    <li><svg viewBox="0 0 16 16"><use href="#tick"/></svg><span>No camping is allowed</span></li>
    <li class="tick-low"><svg viewBox="0 0 16 16"><use href="#tick"/></svg><span>The cellar door bar will not be open during the hours of the wedding unless an approved Pallowmere Estate staff member is on the site whilst open. This will be charged at $25 per hour</span></li>
    <li><svg viewBox="0 0 16 16"><use href="#tick"/></svg><span>Deposit will not be refundable in the event of a cancellation 30 days or more prior to the wedding</span></li>
    <li><svg viewBox="0 0 16 16"><use href="#tick"/></svg><span style="text-align:left">If booking is cancelled less than 30 days and balance<br>has been paid, total amount will be forfeited</span></li>
    <li><svg viewBox="0 0 16 16"><use href="#tick"/></svg><span style="text-align:left">Pallowmere Estate will not be liable for any disruption<br>caused by electrical blackouts, storms or<br>rain periods during your wedding</span></li>
  </ul>

  <svg class="swoosh" width="848" height="1200" viewBox="0 0 848 1200" aria-hidden="true">
    <path d="M0 1140 Q460 1150 848 835 L848 1200 L0 1200 Z" fill="#3bb9ea"/>
    <path d="M0 1146 Q480 1150 848 866 L848 1200 L0 1200 Z" fill="#4a95d6"/>
    <path d="M0 1150 Q500 1155 848 895 L848 1200 L0 1200 Z" fill="#3e5ea9"/>
  </svg>

  <p class="site-url">www.pallowmere.com.au</p>
</div>
</body>
</html>
```